Honeyvale Stitchery Needs a Beautiful Website

I need a new website for this new E-commerce. I sell handmade baby crochets, e.g. booties, headbands, hats, etc. I need a feminine and soft design to make the moms-to-be say 'oohh ahh'. I'd like pink, blue and gray. I'd like an inviting homepage, and nice regular pages where people can see and order the products.

Industry/Entity Type

Baby

Requirements
Must have
• beautiful, soft, feminine design. Please use pictures of the colors I'd like: brown, yellow, pink and blue. Any combination, but definitely include brown.

```html
<!DOCTYPE html>
<html lang="en">
<head>
<meta charset="utf-8">
<title>Honeyvale Stitchery</title>
<link href="https://fonts.googleapis.com/css2?family=Roboto+Slab:wght@400;700&family=Montserrat:wght@400;500;600&family=Roboto:wght@400;700&display=swap" rel="stylesheet">
<style>
:root{
  --bg:#ffc3c9;
  --band:#ffb4bd;
  --band-dark:#ff9fac;
  --panel:#ffe2e6;
  --pink:#ff8c9c;
  --pink-soft:#ff9fb0;
  --teal:#9fe3e8;
  --teal-text:#6fd0da;
  --white:#ffffff;
  --text:#8a7f80;
  --muted:#a89ea0;
}
*{margin:0;padding:0;box-sizing:border-box}
html,body{width:723px;height:1200px;overflow:hidden}
body{position:relative;background:var(--bg);font-family:'Roboto',Arial,sans-serif;color:var(--text)}
.abs{position:absolute}
.header{left:0;top:0;width:723px;height:108px;background:var(--band);box-shadow:0 2px 4px rgba(200,90,110,.25)}
.topbar{left:0;top:0;width:723px;height:21px;border-bottom:1px solid #ffa6b1}
.search{left:325px;top:5px;width:178px;height:12px;background:#ffd3d8;font-size:6px;color:#c98e97;padding:2px 5px;letter-spacing:.5px}
.search svg{position:absolute;right:4px;top:2px}
.signin{left:512px;top:6px;font-size:6px;color:var(--white);letter-spacing:.5px}
.cart{left:547px;top:0;width:89px;height:38px;background:var(--band-dark);border-radius:0 0 4px 4px;text-align:center;color:var(--white);font-size:6px;letter-spacing:.5px}
.cart svg{display:block;margin:5px auto 3px}
.brand{left:95px;top:35px;font-family:'Roboto Slab',serif;font-weight:700;font-size:14px;line-height:16px;color:#ff5f8a;width:110px}
.brand i{display:inline-block;width:8px;height:8px;border-radius:50%;background:#ff5f8a;margin-right:4px;vertical-align:middle}
.nav{left:323px;top:56px;font-family:'Montserrat',sans-serif;font-size:8px;letter-spacing:1.4px;color:var(--white)}
.nav a{color:inherit;text-decoration:none;position:absolute;white-space:nowrap}
.nav a.active{border-bottom:2px solid var(--white);padding-bottom:3px;font-weight:600}
.main{left:40px;top:108px;width:643px;height:920px;background:var(--panel)}
.hero{left:88px;top:79px;width:549px;height:245px;border:2px solid var(--white);background:radial-gradient(ellipse 260px 200px at 80% 40%,#a8d3dc 0%,#c9d6d4 14%,#f1c8b3 26%,#ecd2c0 40%,#e4d9cc 62%,#dcd1c3 100%)}
.hero-copy{left:116px;top:150px;width:180px;text-align:center}
.hero-copy h2{font-family:'Montserrat',sans-serif;font-weight:500;font-size:27px;line-height:31px;letter-spacing:4px;color:#ff8fa0}
.hero-copy p{font-family:'Montserrat',sans-serif;font-weight:600;font-size:12px;letter-spacing:1.6px;color:var(--white);margin-top:1px}
.btn-shop{left:157px;top:236px;width:96px;height:22px;background:var(--pink-soft);color:var(--white);font-family:'Montserrat',sans-serif;font-weight:600;font-size:11px;letter-spacing:1.4px;text-align:center;line-height:22px}
.arrow{top:200px;width:20px;height:20px;border-radius:50%;background:rgba(255,255,255,.8)}
.arrow svg{display:block;margin:5px auto}
.tile{top:336px;width:176px;height:116px;overflow:hidden}
.tile .cap{position:absolute;left:0;bottom:0;width:100%;height:35px;background:rgba(40,40,40,.35);color:var(--white);font-family:'Montserrat',sans-serif;font-size:10px;letter-spacing:1.6px;text-align:center;line-height:38px}
.tile.ship{background:radial-gradient(ellipse at 30% 30%,#5a2a32 0%,#3a3234 45%,#262729 100%);text-align:center;color:var(--white)}
.tile.ship h3{font-family:'Roboto Slab',serif;font-weight:400;font-size:21px;line-height:23px;letter-spacing:2px;margin-top:25px}
.tile.ship p{font-family:'Montserrat',sans-serif;font-size:10px;letter-spacing:.8px}
.featured{left:89px;top:469px;width:420px;height:514px;background:var(--white)}
.bar-title{height:14px;background:var(--pink-soft);color:var(--white);font-family:'Roboto Slab',serif;font-size:7px;letter-spacing:1px;text-align:center;line-height:14px}
.product{width:80px;text-align:center}
.product .name{font-family:'Montserrat',sans-serif;font-size:5.5px;letter-spacing:1px;color:var(--pink);height:12px;line-height:8px}
.product .photo{width:80px;height:78px}
.product .buy{display:flex;height:12px;font-size:5px;line-height:12px;margin-top:-4px;position:relative}
.product .price{width:23px;background:var(--pink-soft);color:var(--white)}
.product .add{flex:1;background:var(--teal);color:#5b8e92;letter-spacing:.5px}
.side{left:519px;width:118px;background:var(--white)}
.side .bar-title{margin:0 -2px}
.side .photo{width:104px;margin:7px auto 0}
.side p{font-size:5.5px;line-height:7px;color:var(--muted);padding:0 7px;margin-top:6px;letter-spacing:.2px}
.save{padding:0 7px;margin-top:6px}
.save small{display:block;font-family:'Montserrat',sans-serif;font-size:7px;line-height:9px;letter-spacing:1.3px;color:var(--pink-soft)}
.save strong{display:block;font-family:'Montserrat',sans-serif;font-weight:600;font-size:20px;line-height:20px;color:var(--teal-text)}
.save span{display:inline-block;background:var(--pink-soft);color:var(--white);font-size:4.5px;padding:1px 3px;letter-spacing:.5px}
.footer{left:0;top:1058px;width:723px;height:142px;background:#ffa8b3}
.footer h4{position:absolute;top:29px;font-family:'Montserrat',sans-serif;font-weight:400;font-size:9px;letter-spacing:1.6px;color:var(--white)}
.footer ul{position:absolute;top:46px;list-style:none;font-size:6.5px;line-height:7.5px;color:var(--white);letter-spacing:.6px}
.social{position:absolute;top:48px;width:14px;height:14px}
.email{position:absolute;left:453px;top:47px;width:151px;height:15px;background:#ffc4cb;font-size:6.5px;color:#ffe9ec;padding:4px 5px;letter-spacing:.5px}
.send{position:absolute;left:604px;top:47px;width:30px;height:15px;background:var(--teal);font-size:6.5px;color:#5b8e92;text-align:center;line-height:15px}
.card{position:absolute;top:79px;width:26px;height:16px;border-radius:2px}
.copyright{position:absolute;left:0;bottom:0;width:723px;height:15px;border-top:1px solid #ffb8c0;font-size:5px;color:var(--white);text-align:center;line-height:15px;letter-spacing:.6px}
</style>
</head>
<body>

<header class="abs header">
  <div class="abs topbar"></div>
  <div class="abs search">Enter a Keyword to Search
    <svg width="8" height="8" viewBox="0 0 8 8"><circle cx="3.2" cy="3.2" r="2.3" fill="none" stroke="#c98e97" stroke-width="1"/><line x1="5" y1="5" x2="7.5" y2="7.5" stroke="#c98e97" stroke-width="1.2"/></svg>
  </div>
  <div class="abs signin">Sign in »</div>
  <div class="abs cart">
    <svg width="24" height="18" viewBox="0 0 24 18"><path d="M1 2h4l3 10h12l2-7H7" fill="none" stroke="#fff" stroke-width="1.6" stroke-linejoin="round"/><circle cx="10" cy="15.5" r="1.6" fill="#fff"/><circle cx="18" cy="15.5" r="1.6" fill="#fff"/></svg>
    0 item(s) - $0.00
  </div>
  <div class="abs brand"><i></i>Honeyvale Stitchery</div>
  <nav class="abs nav">
    <a class="active" style="left:0">HOME</a>
    <a style="left:50px">PRODUCT</a>
    <a style="left:117px">ABOUT</a>
    <a style="left:170px">PAGES</a>
    <a style="left:222px">BLOG</a>
    <a style="left:269px">CONTACT</a>
  </nav>
</header>

<div class="abs main"></div>

<section class="abs hero" role="img" aria-label="Sleeping newborn wearing a light blue crochet crown on a soft beige blanket"></section>
<div class="abs hero-copy"><h2>NEW<br>ARRIVALS</h2><p>GET UP TO 10% OFF</p></div>
<div class="abs btn-shop">SHOP NOW!</div>
<div class="abs arrow" style="left:79px"><svg width="8" height="10" viewBox="0 0 8 10"><path d="M6 1L2 5l4 4" fill="none" stroke="#b9a9a9" stroke-width="1.5"/></svg></div>
<div class="abs arrow" style="left:624px"><svg width="8" height="10" viewBox="0 0 8 10"><path d="M2 1l4 4-4 4" fill="none" stroke="#b9a9a9" stroke-width="1.5"/></svg></div>

<div class="abs tile" style="left:89px;background:radial-gradient(ellipse 120px 80px at 55% 60%,#f0c8b8 0%,#d9b3c0 30%,#a590d6 60%,#8a76c8 100%)" role="img" aria-label="Baby asleep in a gray crochet crown on a purple blanket"><div class="cap">ON SALE</div></div>
<div class="abs tile" style="left:276px;background:radial-gradient(ellipse 120px 80px at 40% 45%,#9fb3a4 0%,#e8c9b0 28%,#eadccb 55%,#c9ae8e 100%)" role="img" aria-label="Baby in a sage green crochet beanie lying on white sheets"><div class="cap">SPECIAL OFFERS</div></div>
<div class="abs tile ship" style="left:462px"><h3>FREE<br>SHIPPING</h3><p>on orders over $99.</p></div>

<section class="abs featured">
  <div class="bar-title">FEATURED PRODUCTS</div>
</section>

<div class="abs product" style="left:102px;top:495px"><div class="name">LOREM IPSUM</div><div class="photo" role="img" aria-label="Pink crochet crown headband" style="background:radial-gradient(ellipse 34px 22px at 50% 48%,#ff8fc4 0%,#ffa8d0 55%,#e6dfe1 100%)"></div><div class="buy"><span class="price">$14.99</span><span class="add">Add to cart</span></div></div>
<div class="abs product" style="left:207px;top:495px"><div class="name">LOREM IPSUM</div><div class="photo" role="img" aria-label="Turquoise crochet crown headband" style="background:radial-gradient(ellipse 34px 22px at 50% 48%,#4fd4e6 0%,#8fdfe8 55%,#e4e4e4 100%)"></div><div class="buy"><span class="price">$14.99</span><span class="add">Add to cart</span></div></div>
<div class="abs product" style="left:312px;top:495px"><div class="name">LOREM IPSUM</div><div class="photo" role="img" aria-label="Magenta crochet crown headband" style="background:radial-gradient(ellipse 34px 22px at 50% 48%,#ee5ad8 0%,#f29ae6 55%,#e4e2e4 100%)"></div><div class="buy"><span class="price">$14.99</span><span class="add">Add to cart</span></div></div>
<div class="abs product" style="left:417px;top:495px"><div class="name">LOREM IPSUM</div><div class="photo" role="img" aria-label="Hot pink crochet crown headband" style="background:radial-gradient(ellipse 34px 22px at 50% 48%,#f02c78 0%,#f27aa6 55%,#e2dfe0 100%)"></div><div class="buy"><span class="price">$14.99</span><span class="add">Add to cart</span></div></div>

<div class="abs product" style="left:102px;top:619px"><div class="name">LOREM IPSUM</div><div class="photo" role="img" aria-label="Black crochet sneaker booties" style="background:radial-gradient(ellipse at 50% 55%,#2a2a2a 0%,#555 45%,#c9c9c9 100%)"></div><div class="buy"><span class="price">$14.99</span><span class="add">Add to cart</span></div></div>
<div class="abs product" style="left:207px;top:619px"><div class="name">LOREM IPSUM</div><div class="photo" role="img" aria-label="Brown crochet sneaker booties with red star" style="background:radial-gradient(ellipse at 50% 55%,#5c4238 0%,#7a6058 45%,#6a4a5c 100%)"></div><div class="buy"><span class="price">$14.99</span><span class="add">Add to cart</span></div></div>
<div class="abs product" style="left:312px;top:619px"><div class="name">LOREM IPSUM</div><div class="photo" role="img" aria-label="Navy crochet sneaker booties" style="background:radial-gradient(ellipse at 50% 55%,#34406a 0%,#5a6280 45%,#9a9a9e 100%)"></div><div class="buy"><span class="price">$14.99</span><span class="add">Add to cart</span></div></div>
<div class="abs product" style="left:417px;top:619px"><div class="name">LOREM IPSUM</div><div class="photo" role="img" aria-label="Red crochet sneaker booties" style="background:radial-gradient(ellipse at 50% 55%,#e2402a 0%,#c0584a 45%,#8a8282 100%)"></div><div class="buy"><span class="price">$14.99</span><span class="add">Add to cart</span></div></div>

<div class="abs product" style="left:102px;top:743px"><div class="name">LOREM IPSUM</div><div class="photo" role="img" aria-label="Pink and white crochet slippers with roses" style="background:radial-gradient(ellipse at 50% 60%,#f4b8c4 0%,#efd6da 45%,#e0d8d8 100%)"></div><div class="buy"><span class="price">$14.99</span><span class="add">Add to cart</span></div></div>
<div class="abs product" style="left:207px;top:743px"><div class="name">LOREM IPSUM</div><div class="photo" role="img" aria-label="White crochet ballet booties with ribbons" style="background:radial-gradient(ellipse at 50% 55%,#f2ecea 0%,#cfc8c6 35%,#3a3434 70%,#1c1a1a 100%)"></div><div class="buy"><span class="price">$14.99</span><span class="add">Add to cart</span></div></div>
<div class="abs product" style="left:312px;top:743px"><div class="name">LOREM IPSUM</div><div class="photo" role="img" aria-label="Red crochet Mary Jane booties" style="background:radial-gradient(ellipse at 50% 60%,#d0302a 0%,#a2322e 45%,#3e4440 100%)"></div><div class="buy"><span class="price">$14.99</span><span class="add">Add to cart</span></div></div>
<div class="abs product" style="left:417px;top:743px"><div class="name">LOREM IPSUM</div><div class="photo" role="img" aria-label="Teal crochet Mary Jane booties" style="background:radial-gradient(ellipse at 50% 60%,#40b8c0 0%,#3a8c92 45%,#3a4442 100%)"></div><div class="buy"><span class="price">$14.99</span><span class="add">Add to cart</span></div></div>

<div class="abs product" style="left:102px;top:868px"><div class="name">LOREM IPSUM</div><div class="photo" role="img" aria-label="Cream crochet booties with pink flowers" style="background:radial-gradient(ellipse at 50% 55%,#e4dccc 0%,#c8bfae 40%,#555 100%)"></div><div class="buy"><span class="price">$14.99</span><span class="add">Add to cart</span></div></div>
<div class="abs product" style="left:207px;top:868px"><div class="name">LOREM IPSUM</div><div class="photo" role="img" aria-label="Ivory crochet sandals with red flowers" style="background:radial-gradient(ellipse at 50% 55%,#e6e0d2 0%,#c6beb0 40%,#525050 100%)"></div><div class="buy"><span class="price">$14.99</span><span class="add">Add to cart</span></div></div>
<div class="abs product" style="left:312px;top:868px"><div class="name">LOREM IPSUM</div><div class="photo" role="img" aria-label="Gray crochet booties with red rose" style="background:radial-gradient(ellipse at 55% 60%,#9a9696 0%,#6e6a6a 45%,#3a3a3a 100%)"></div><div class="buy"><span class="price">$14.99</span><span class="add">Add to cart</span></div></div>
<div class="abs product" style="left:417px;top:868px"><div class="name">LOREM IPSUM</div><div class="photo" role="img" aria-label="Gray crochet Mary Jane booties" style="background:radial-gradient(ellipse at 50% 55%,#a8a4a4 0%,#7a7676 45%,#3c3c3c 100%)"></div><div class="buy"><span class="price">$14.99</span><span class="add">Add to cart</span></div></div>

<aside class="abs side" style="top:469px;height:164px">
  <div class="bar-title">BEST SELLERS</div>
  <div class="photo" style="height:100px;background:radial-gradient(ellipse at 40% 45%,#e8a8b0 0%,#c8d8e0 35%,#b05060 70%,#5a4a4a 100%)" role="img" aria-label="Collage of colorful crochet baby shoes"></div>
  <p>Lorem ipsum dolor sit amet, consectetur adipisicing elit, sed do eiusmod tempor incididunt ut labore et dolore magna aliqua.</p>
</aside>

<aside class="abs side" style="top:651px;height:214px">
  <div class="bar-title">WINTER COLLECTIONS</div>
  <div class="photo" style="height:105px;background:radial-gradient(ellipse at 50% 50%,#d8d8dc 0%,#9aa4b4 35%,#c85a64 60%,#4a4a50 100%)" role="img" aria-label="Collage of crochet sneaker booties in winter colors"></div>
  <div class="save"><small>SAVE UP TO</small><strong>20%</strong><span>SHOP NOW!</span></div>
  <p style="margin-top:4px">Lorem ipsum dolor sit amet, consectetur adipisicing elit, sed do eiusmod tempor incididunt ut labore et dolore magna aliqua.</p>
</aside>

<aside class="abs side" style="top:880px;height:103px">
  <div class="bar-title">TESTIMONIALS</div>
  <p style="margin-top:8px">"Lorem ipsum dolor sit amet, consectetur adipisicing elit, sed do eiusmod tempor incididunt ut labore et dolore magna aliqua."</p>
  <p style="margin-top:6px">- Mara Ellison -</p>
</aside>

<footer class="abs footer">
  <h4 style="left:89px">BROWSE</h4>
  <ul style="left:89px"><li>Home</li><li>Products</li><li>Page</li><li>Blog</li><li>Contact</li><li>Login</li></ul>
  <h4 style="left:188px">SITE INFO</h4>
  <ul style="left:189px"><li>About us</li><li>Customer Testimonials</li><li>Shipping Details</li><li>Privacy</li><li>Terms &amp; Conditions</li><li>Subscribe</li></ul>
  <h4 style="left:328px">FOLLOW US</h4>
  <span class="social" style="left:329px;background:#3b5a98"></span>
  <span class="social" style="left:349px;background:#3fa6e0"></span>
  <h4 style="left:453px">GET EMAIL EXCLUSIVES</h4>
  <div class="email">Enter Email Address</div>
  <div class="send">Send</div>
  <span class="card" style="left:519px;background:#3a7ac0"></span>
  <span class="card" style="left:548px;background:#f0f0f0"></span>
  <span class="card" style="left:577px;background:#d8343a"></span>
  <span class="card" style="left:608px;background:#f4f4f4"></span>
  <div class="copyright">Honeyvale Stitchery · ©2014 · All rights reserved</div>
</footer>

</body>
</html>
```